Design Build and Remodeling Contractors....needs Flyer Design

We need flyer design for residential construction services. We would like the design to be appealing and stand out amongst a hand full of other mailers. Colors we would like to implement are navy blue and fluorescent/highlighter yellow. We have uploaded our company logo and phone number.

Industry/Entity Type

Residential

```html
<!DOCTYPE html>
<html lang="en">
<head>
<meta charset="utf-8">
<title>Keystone Build Services Flyer</title>
<link href="https://fonts.googleapis.com/css2?family=Roboto+Condensed:wght@400;700&family=Lato:wght@400&display=swap" rel="stylesheet">
<style>
  :root {
    --navy: #1414b4;
    --navy-deep: #08087e;
    --hi-yellow: #ffff00;
    --frame-yellow: #f6f30c;
    --ink: #1e1e1e;
    --white: #ffffff;
  }
  * { margin: 0; padding: 0; box-sizing: border-box; }
  html, body { width: 900px; height: 1200px; overflow: hidden; background: #e8e8e8; }
  .flyer {
    position: relative;
    width: 900px;
    height: 1200px;
    overflow: hidden;
    font-family: "Roboto Condensed", "Arial Narrow", sans-serif;
  }
  .flyer-art { position: absolute; inset: 0; }
  .brand-name {
    position: absolute;
    left: 28px; top: 178px;
    width: 360px;
    text-align: center;
    font-weight: 400;
    font-size: 30px;
    letter-spacing: 1.5px;
    line-height: 1.15;
    color: var(--ink);
  }
  .headline {
    position: absolute;
    right: 46px; top: 52px;
    text-align: right;
    font-weight: 700;
    line-height: 0.92;
  }
  .headline .line-small { display: block; font-size: 62px; color: var(--hi-yellow); }
  .headline .line-big { display: block; font-size: 112px; color: var(--hi-yellow); margin-top: 4px; }
  .headline .line-white { display: block; font-size: 92px; color: var(--white); margin-top: 0; }
  .about {
    position: absolute;
    left: 27px; top: 886px;
    width: 490px;
  }
  .about-title {
    font-weight: 700;
    font-size: 25px;
    color: var(--navy-deep);
    margin-bottom: 14px;
  }
  .about-text {
    font-family: "Lato", "Helvetica", sans-serif;
    font-size: 16px;
    line-height: 20.5px;
    color: var(--ink);
  }
  .call {
    position: absolute;
    right: 28px; top: 916px;
    text-align: right;
    font-weight: 700;
  }
  .call-label { font-size: 58px; color: var(--hi-yellow); line-height: 1; }
  .call-number { font-size: 50px; color: var(--white); line-height: 1.1; margin-top: 6px; }
  .footer-item {
    position: absolute;
    top: 1116px;
    display: flex;
    align-items: center;
    gap: 14px;
    font-weight: 700;
    font-size: 22px;
    color: #101040;
  }
  .footer-address { left: 30px; }
  .footer-web { right: 26px; }
  .footer-item svg { width: 24px; height: 24px; }
</style>
</head>
<body>
<main class="flyer">
  <svg class="flyer-art" width="900" height="1200" viewBox="0 0 900 1200">
    <defs>
      <linearGradient id="grey-panel" x1="0" y1="0" x2="0.4" y2="1">
        <stop offset="0" stop-color="#bdbdbd"/>
        <stop offset="0.6" stop-color="#f2f2f2"/>
        <stop offset="1" stop-color="#ffffff"/>
      </linearGradient>
      <linearGradient id="grey-lower" x1="0" y1="0" x2="0" y2="1">
        <stop offset="0" stop-color="#ffffff"/>
        <stop offset="1" stop-color="#d8d8d8"/>
      </linearGradient>
      <linearGradient id="navy-panel" x1="0" y1="0" x2="1" y2="1">
        <stop offset="0" stop-color="#1a1ad0"/>
        <stop offset="1" stop-color="#0a0a8a"/>
      </linearGradient>
      <linearGradient id="photo-team" x1="0" y1="0" x2="0" y2="1">
        <stop offset="0" stop-color="#dfe8ef"/>
        <stop offset="0.4" stop-color="#7ea35a"/>
        <stop offset="0.7" stop-color="#c9d660"/>
        <stop offset="1" stop-color="#6d8fb6"/>
      </linearGradient>
      <linearGradient id="photo-house" x1="0" y1="0" x2="0" y2="1">
        <stop offset="0" stop-color="#2f64b7"/>
        <stop offset="0.55" stop-color="#a9c6e6"/>
        <stop offset="0.62" stop-color="#5e9a2c"/>
        <stop offset="1" stop-color="#2f7a19"/>
      </linearGradient>
      <linearGradient id="photo-worker" x1="0" y1="0" x2="1" y2="1">
        <stop offset="0" stop-color="#e4e4e4"/>
        <stop offset="0.5" stop-color="#3a3f48"/>
        <stop offset="1" stop-color="#5a6a86"/>
      </linearGradient>
    </defs>

    <rect class="panel-top" x="0" y="0" width="900" height="340" fill="url(#grey-panel)"/>
    <rect class="panel-lower" x="0" y="820" width="900" height="380" fill="url(#grey-lower)"/>
    <polygon class="navy-top" points="483,0 900,0 900,340 379,340" fill="url(#navy-panel)"/>
    <polygon class="navy-lower" points="643,820 900,820 900,1200 483,1200 523,1090" fill="url(#navy-panel)"/>

    <polygon class="frame" points="0,313 390,313 232,830 0,830" fill="var(--frame-yellow)"/>
    <polygon class="frame" points="372,330 752,330 585,818 205,818" fill="var(--frame-yellow)"/>
    <polygon class="frame" points="740,345 900,345 900,818 565,818" fill="var(--frame-yellow)"/>

    <g role="img" aria-label="Photo: two construction engineers in hard hats reviewing a tablet outdoors">
      <polygon points="0,330 368,330 212,830 0,830" fill="url(#photo-team)"/>
    </g>
    <g role="img" aria-label="Photo: a hand holding a small model house over green grass and blue sky">
      <polygon points="392,348 732,348 568,805 222,805" fill="url(#photo-house)"/>
    </g>
    <g role="img" aria-label="Photo: a builder in a yellow hard hat working with a screwdriver">
      <polygon points="748,365 900,365 900,802 582,802" fill="url(#photo-worker)"/>
    </g>

    <rect class="footer-band" x="0" y="1090" width="900" height="80" fill="var(--hi-yellow)"/>
  </svg>

  <div class="brand-name">KEYSTONE<br>BUILD SERVICES INC</div>

  <h1 class="headline">
    <span class="line-small">LOREM IPSUM</span>
    <span class="line-big">DOLOR</span>
    <span class="line-white">SIT AMET</span>
  </h1>

  <section class="about">
    <h2 class="about-title">ABOUT US</h2>
    <p class="about-text">Lorem ipsum dolor sit amet, nemore vidisse eam eu, solet sanctus cum et. Vim an nonumes dolorem sadipscing, vis id quod mandamus intellegebat. Cetero docendi tincidunt sea an, cu oratio constituam sea, justo corrumpit ea mei. Mel legere timeam te, quidam appellantur no mei, id movet numquam incorrupte nec. Cu cibo moderatius mel.</p>
  </section>

  <div class="call">
    <div class="call-label">CALL TODAY</div>
    <div class="call-number">800-555-0142</div>
  </div>

  <div class="footer-item footer-address">
    <svg viewBox="0 0 24 24" aria-hidden="true"><path d="M12 3 2 12h3v9h5v-6h4v6h5v-9h3z" fill="var(--navy)"/></svg>
    <span>PO BOX 482 ALDER CA 90000</span>
  </div>
  <div class="footer-item footer-web">
    <svg viewBox="0 0 24 24" aria-hidden="true">
      <circle cx="12" cy="12" r="9.5" fill="none" stroke="var(--navy)" stroke-width="2"/>
      <ellipse cx="12" cy="12" rx="4" ry="9.5" fill="none" stroke="var(--navy)" stroke-width="1.6"/>
      <path d="M2.5 12h19M4 7h16M4 17h16" stroke="var(--navy)" stroke-width="1.6"/>
    </svg>
    <span>WWW.YOURDOMAIN.COM</span>
  </div>
</main>
</body>
</html>
```